Patent Law

Need to develop a home page for a patent lawyer.

Colors should go with logo, blues...

Company Name- Velric Dunmore, PLLC

Company Overview-

I am an Intellectual Property Lawyer and focus on patents, copyrights, trademarks, & trade secrets. I work with small businesses and start ups in the chemical and biotech industries.

Why Us-

I am small firm that can provide large-firm service at a reasonable price. I also can charge flat-fees for entreprenuers in certain practice areas.

Services-
Intellectual Property
Patents
Copyrights
Trademarks
Trade secrets
Healthcare Compliance
Elder law
Wills
Trusts

Website we like-
http://www.tolvanecrest.com/ - within industry!!
http://www.quarnhollet.com/
http://brevicktallon.com/
http://thegravelwrights.com/

Target Market(s)

My customers will be small business, specifically small start-up companies in the chemical and biotech arena.

Industry/Entity Type

Trade

Requirements
Must have
• Colors should go with logo, blues...

```html
<!DOCTYPE html>
<html lang="en">
<head>
<meta charset="utf-8">
<title>Velric Dunmore, PLLC — Intellectual Property Law</title>
<link rel="stylesheet" href="https://fonts.googleapis.com/css2?family=Noto+Serif:wght@400;700&family=Arimo:wght@400;700&display=swap">
<style>
:root{
  --blue-bright:#0a9ad6;
  --blue-royal:#3553a3;
  --blue-deep:#2f4a9a;
  --blue-band-top:#0b7bc6;
  --blue-band-bottom:#2f4fa2;
  --ink:#333333;
  --grey-line:#b9c3c8;
  --footer-grey:#7f8c95;
  --social-grey:#6b767e;
  --white:#ffffff;
}
*{margin:0;padding:0;box-sizing:border-box}
html,body{width:1200px;height:1090px;overflow:hidden;background:var(--white)}
body{position:relative;font-family:"Noto Serif",Georgia,serif;color:var(--ink)}
.abs{position:absolute}

/* header */
.phone-top{left:150px;top:36px;display:flex;align-items:center;gap:10px;font-size:17px;color:#444}
.search{left:825px;top:41px;width:225px;height:33px;display:flex}
.search-input{flex:1;border:1px solid #ccd3d7;border-right:none;border-radius:17px 0 0 17px;font-size:13px;color:#9a9a9a;padding:8px 0 0 17px}
.search-btn{width:70px;background:var(--blue-deep);color:var(--white);border-radius:0 17px 17px 0;font-size:13.5px;text-align:center;padding-top:8px}
.brand-mark{left:578px;top:50px;width:44px;height:44px;border-radius:50%;background:var(--blue-royal)}
.header-rule{top:116px;height:1px;background:var(--grey-line)}
.header-rule.left{left:150px;width:345px}
.header-rule.right{left:705px;width:345px}
.brand-name{top:106px;left:0;width:1200px;text-align:center;font-size:15px;color:#4a5560;letter-spacing:.3px}
.nav{top:139px;left:0;width:1200px;display:flex;justify-content:center;font-size:14.5px}
.nav a{color:#333;text-decoration:none;padding:0 18px;line-height:34px;border-right:1px dotted #9aa4aa}
.nav a:last-child{border-right:none}
.nav a.current{color:var(--blue-bright)}

/* hero */
.hero-band{left:0;top:198px;width:1200px;height:303px;background:linear-gradient(var(--blue-band-top),var(--blue-band-bottom))}
.hero{left:150px;top:182px;width:900px;height:334px;background:linear-gradient(90deg,#fafafa 0%,#efecea 40%,#d9cfc6 62%,#c9b49a 80%,#d8c46a 88%,#b39c80 100%)}
.hero-shadow{left:290px;top:514px;width:620px;height:10px;border-radius:50%;background:radial-gradient(ellipse at center,rgba(0,0,0,.55),rgba(0,0,0,0) 70%)}
.hero-title{left:187px;top:271px;font-family:"Arimo",Arial,sans-serif;font-weight:700;font-size:36px;line-height:34px;color:var(--blue-bright)}
.hero-text{left:187px;top:356px;width:310px;font-size:13.5px;line-height:22.5px;color:#222}
.hero-more{left:187px;top:434px;font-size:14px;color:var(--blue-royal);display:flex;align-items:center;gap:5px}

/* content */
.section-title{font-family:"Arimo",Arial,sans-serif;font-weight:400;font-size:29px;color:var(--blue-royal)}
.why{left:149px;top:556px;width:438px}
.why p{font-size:13.5px;line-height:22.5px;margin-top:14px}
.why p + p{margin-top:22px}
.why a{color:var(--blue-bright);text-decoration:none}
.services{left:614px;top:556px;width:204px}
.services ul{list-style:none;margin-top:12px}
.services li{height:28px;border-bottom:1px dotted #b0b8bd;font-size:13.5px;color:var(--blue-bright);padding:5px 0 0 16px;position:relative}
.services li::before{content:"";position:absolute;left:5px;top:12px;border:3px solid transparent;border-left:4px solid var(--blue-bright)}
.contact{left:847px;top:562px;width:203px;height:286px;background:var(--blue-deep);color:var(--white);text-align:center}
.contact h2{font-family:"Arimo",Arial,sans-serif;font-weight:700;font-size:35px;line-height:36px;color:#14b4ee;margin-top:20px}
.contact h3{font-family:"Arimo",Arial,sans-serif;font-weight:700;font-size:23px;line-height:24px}
.contact address{font-style:normal;font-size:13.5px;line-height:22.5px;margin-top:16px}
.contact .line{display:flex;justify-content:center;align-items:center;gap:7px;font-size:13.5px;margin-top:13px}
.contact .line.email{font-size:12.5px;gap:6px}
.contact .link{color:#8fd2f5}

/* footer */
.footer{left:150px;top:895px;width:900px;height:118px}
.copyright{left:169px;top:946px;font-size:12px;color:var(--white)}
.socials{left:894px;top:934px;display:flex;gap:5px}
.socials span{width:45px;height:42px;background:var(--social-grey)}
.footer-badge{left:556px;top:976px;width:88px;height:88px;border-radius:50%;background:var(--white)}
.footer-mark{left:584px;top:994px;width:32px;height:32px;border-radius:50%;background:var(--blue-royal)}
.footer-name{left:0;width:1200px;top:1057px;text-align:center;font-size:13.5px;color:#4a5560}
</style>
</head>
<body>

<header>
  <div class="abs phone-top">
    <svg width="26" height="46" viewBox="0 0 26 46" aria-hidden="true"><rect x="0" y="0" width="26" height="46" rx="4" fill="#111"/><rect x="4" y="7" width="18" height="28" fill="#fff"/><circle cx="13" cy="40" r="2" fill="#fff"/></svg>
    <span>555-210-7741</span>
  </div>
  <div class="abs brand-mark"></div>
  <div class="abs header-rule left"></div>
  <div class="abs header-rule right"></div>
  <div class="abs brand-name">VELRIC DUNMORE, PLLC</div>
  <div class="abs search"><div class="search-input">Enter Keyword</div><div class="search-btn">Search</div></div>
  <nav class="abs nav">
    <a class="current" href="#">HOME</a><a href="#">ABOUT US</a><a href="#">SERVICES</a><a href="#">RESOURCES</a><a href="#">FEES</a><a href="#">BLOG</a><a href="#">CONTACT US</a>
  </nav>
</header>

<section>
  <div class="abs hero-band"></div>
  <div class="abs hero" role="img" aria-label="Photo of a scientist in safety goggles pouring yellow liquid from a test tube into a beaker"></div>
  <div class="abs hero-shadow"></div>
  <h1 class="abs hero-title">LOREM IPSUM IS<br>SIMPLY DUMMY</h1>
  <p class="abs hero-text">Lorem Ipsum has been the industry's standard dummy text ever since the 1500s, when an unknown printer took a galley.</p>
  <div class="abs hero-more">Read More
    <svg width="20" height="20" viewBox="0 0 20 20" aria-hidden="true"><circle cx="10" cy="10" r="8.5" fill="none" stroke="#0a9ad6" stroke-width="2"/><path d="M6 10h7M10 7l3 3-3 3" fill="none" stroke="#0a9ad6" stroke-width="1.6"/></svg>
  </div>
</section>

<main>
  <section class="abs why">
    <h2 class="section-title">WHY US</h2>
    <p>Lorem Ipsum is simply dummy text of the printing and typesetting industry. Lorem Ipsum has been the industry's standard dummy text ever since the 1500s, when an unknown printer took a galley of type and scrambled it to make a type specimen book. It has survived not only five centuries, but also the leap into electronic typesetting, remaining essentially unchanged.</p>
    <p>It was popularised in the 1960s with the release of Tessaline sheets containing Lorem Ipsum passages, and more recently with desktop publishing software like Quillform Layout including versions of Lorem Ipsum. <a href="#">Read More ▸</a></p>
  </section>

  <section class="abs services">
    <h2 class="section-title">WHAT WE DO</h2>
    <ul>
      <li>Intellectual Property</li><li>Patents</li><li>Copyrights</li><li>Trademarks</li><li>Trade secrets</li><li>Healthcare Compliance</li><li>Elder law</li><li>Wills</li><li>Trusts</li>
    </ul>
  </section>

  <aside class="abs contact">
    <h2>CONTACT</h2>
    <h3>INFORMATION</h3>
    <address>Corvin T. Hallam<br>48 Larkspur Lane<br>Brenholt, TX 77411</address>
    <div class="line"><svg width="12" height="20" viewBox="0 0 12 20" aria-hidden="true"><rect width="12" height="20" rx="2" fill="#fff"/><rect x="2" y="3" width="8" height="12" fill="#2f4a9a"/></svg>555-210-7741</div>
    <div class="line link email"><svg width="18" height="12" viewBox="0 0 20 13" aria-hidden="true"><rect width="20" height="13" fill="#fff"/><path d="M0 0l10 7 10-7" fill="none" stroke="#2f4a9a" stroke-width="1.5"/></svg>info@velricdunmore.com</div>
    <div class="line link"><svg width="16" height="18" viewBox="0 0 16 18" aria-hidden="true"><path d="M8 18C3 12 1 9 1 7a7 7 0 0 1 14 0c0 2-2 5-7 11z" fill="#fff"/><circle cx="8" cy="7" r="2.5" fill="#2f4a9a"/></svg>Location Map</div>
  </aside>
</main>

<footer>
  <svg class="abs footer" viewBox="0 0 900 118" aria-hidden="true"><path d="M38 0H862L900 38V118H0V38Z" fill="#7f8c95"/></svg>
  <p class="abs copyright">Copyright © 2014, <b>Velric Dunmore, PLLC.</b> All rights reserved</p>
  <div class="abs socials" aria-label="Social links"><span></span><span></span><span></span></div>
  <div class="abs footer-badge"></div>
  <div class="abs footer-mark"></div>
  <div class="abs footer-name">VELRIC DUNMORE, PLLC</div>
</footer>

</body>
</html>
```